Online shopping portal - Business Card Design

Brivanto.com.au is a complete shopping experience. Search, compare & buy items from partnered stores & receive cashbash for your purchases and referrals.
Mission
Our mission is to provide a system for entrepreneurs to create an ongoing income, while providing consumers worldwide with a better way to shop.
A product brokerage and Internet marketing company that specialises in One-to-One Marketing, Quelden Australia is a subsidiary of Quelden Norvik Worldwide, Inc.
With more than 3 million Preferred Customers and 180,000 Customer Managers worldwide, Quelden Norvik has generated over $3 billion USD in accumulated retail sales. The Company employs more than 675 people globally with international operations in Australia, United States, Canada, Taiwan, Hong Kong, Mexico & Singapore
Through revolutionary technology and the one-to-one marketing and social shopping Quelden Australia are leveraging the Internet with the power of people to create the economy of the future.
By providing online shoppers with the products and services they want and need — backed by the Company’s people power — Quelden Australia is fast becoming the World Wide Web’s ultimate online shopping destination.
As a result, we are changing the way people shop and changing the economic paradigm where anyone can become financially independent by creating their own economy — Rooted in Goods. Lifted by Folk®.
Description
Welcome to a new kind of comparison shopping site where you get PAID cashback to shop!
Simply create an account to start accumulating cash backs each time you make purchases across hundreds of trusted Partner Stores and thousands of your favorite brands through our convenient SwiftTote® for one stop shopping.
All merchant stores are backed by PELMARO.COM's 100% satisfaction guarantee.

Updates
Project Deadline Extended
Reason: Hi all,  I am extending the deadline as i'm going to be away for my birthday (and may not have time to check before the current deadline anyway)  I figure that the more time i give you the better.

Industry/Entity Type
Online Shopping
Contact Information for Business Card
Business Name: Brivanto.com.au
website: www.brivanto.com.au
Facebook: www.facebook.com/brivanto.com.au.
Email: info@brivanto.com.au
Phone: Mirel on 0497 28 14 56
Requirements
Nice to have
- Create a Brivanto logo

```html
<!DOCTYPE html>
<html lang="en">
<head>
<meta charset="utf-8">
<title>Brivanto.com.au – Business Card</title>
<link rel="stylesheet" href="https://fonts.googleapis.com/css2?family=Montserrat:wght@400;600;700&display=swap">
<style>
  :root {
    --bg: #e9e8e6;
    --blue: #1ea6de;
    --green: #62b24a;
    --brand-green: #4aab3c;
    --white: #ffffff;
    --ink: #4aab3c;
    --shadow: 0 14px 30px rgba(0,0,0,0.22);
  }
  * { margin: 0; padding: 0; box-sizing: border-box; }
  html, body { width: 896px; height: 1200px; overflow: hidden; }
  body {
    background: var(--bg);
    font-family: "Montserrat", Arial, sans-serif;
    position: relative;
  }
  .variant { position: absolute; left: 0; width: 896px; height: 600px; }
  .variant--blue { top: 0; }
  .variant--green { top: 600px; }

  .card {
    position: absolute;
    width: 400px;
    height: 240px;
    border-radius: 4px;
    box-shadow: var(--shadow);
  }
  .card--front { left: 50px; top: 90px; color: var(--white); }
  .variant--blue .card--front { background: var(--blue); }
  .variant--green .card--front { background: var(--green); }
  .card--back { left: 446px; top: 260px; background: var(--white); color: var(--ink); text-align: center; }

  .brand-mark {
    width: 58px; height: 58px; border-radius: 50%;
    border: 5px solid currentColor;
  }
  .card--front .brand-mark { position: absolute; left: 40px; top: 30px; }
  .card--front .brand-name {
    position: absolute; left: 40px; top: 102px;
    font-weight: 700; font-size: 24px; letter-spacing: 0.2px;
  }
  .features {
    position: absolute; left: 40px; top: 150px;
    display: flex; gap: 34px; list-style: none;
  }
  .feature { display: flex; flex-direction: column; align-items: center; gap: 6px; }
  .feature svg { width: 30px; height: 30px; }
  .feature span { font-size: 12px; font-weight: 600; }

  .card--back .brand-mark {
    margin: 26px auto 0; border-color: var(--brand-green); width: 62px; height: 62px;
  }
  .card--back .brand-name {
    margin-top: 10px; font-weight: 700; font-size: 24px; color: var(--brand-green);
  }
  .contact-lines { margin-top: 8px; list-style: none; font-size: 10px; line-height: 1.45; font-weight: 400; }
  .contact-phone { margin-top: 10px; font-size: 16px; font-weight: 600; letter-spacing: 0.5px; }
</style>
</head>
<body>

<section class="variant variant--blue">
  <article class="card card--front">
    <div class="brand-mark" aria-hidden="true"></div>
    <div class="brand-name">Brivanto.com.au</div>
    <ul class="features">
      <li class="feature">
        <svg viewBox="0 0 30 30" fill="none" stroke="currentColor" stroke-width="3" stroke-linecap="round"><circle cx="12" cy="12" r="8"/><line x1="18" y1="18" x2="26" y2="26"/></svg>
        <span>Search</span>
      </li>
      <li class="feature">
        <svg viewBox="0 0 30 30" fill="none" stroke="currentColor" stroke-width="3" stroke-linecap="round" stroke-linejoin="round"><polyline points="4,10 24,10 19,5"/><polyline points="26,20 6,20 11,25"/></svg>
        <span>Compare</span>
      </li>
      <li class="feature">
        <svg viewBox="0 0 30 30" fill="none" stroke="currentColor" stroke-width="3" stroke-linejoin="round"><path d="M5 11 H25 L22 26 H8 Z"/><path d="M10 11 V8 a5 5 0 0 1 10 0 V11"/></svg>
        <span>Buy</span>
      </li>
    </ul>
  </article>
  <article class="card card--back">
    <div class="brand-mark" aria-hidden="true"></div>
    <div class="brand-name">Brivanto.com.au</div>
    <ul class="contact-lines">
      <li>www.brivanto.com.au</li>
      <li>www.facebook.com/brivanto.com.au.</li>
      <li>info@brivanto.com.au</li>
    </ul>
    <div class="contact-phone">0497 28 14 56</div>
  </article>
</section>

<section class="variant variant--green">
  <article class="card card--front">
    <div class="brand-mark" aria-hidden="true"></div>
    <div class="brand-name">Brivanto.com.au</div>
    <ul class="features">
      <li class="feature">
        <svg viewBox="0 0 30 30" fill="none" stroke="currentColor" stroke-width="3" stroke-linecap="round"><circle cx="12" cy="12" r="8"/><line x1="18" y1="18" x2="26" y2="26"/></svg>
        <span>Search</span>
      </li>
      <li class="feature">
        <svg viewBox="0 0 30 30" fill="none" stroke="currentColor" stroke-width="3" stroke-linecap="round" stroke-linejoin="round"><polyline points="4,10 24,10 19,5"/><polyline points="26,20 6,20 11,25"/></svg>
        <span>Compare</span>
      </li>
      <li class="feature">
        <svg viewBox="0 0 30 30" fill="none" stroke="currentColor" stroke-width="3" stroke-linejoin="round"><path d="M5 11 H25 L22 26 H8 Z"/><path d="M10 11 V8 a5 5 0 0 1 10 0 V11"/></svg>
        <span>Buy</span>
      </li>
    </ul>
  </article>
  <article class="card card--back">
    <div class="brand-mark" aria-hidden="true"></div>
    <div class="brand-name">Brivanto.com.au</div>
    <ul class="contact-lines">
      <li>www.brivanto.com.au</li>
      <li>www.facebook.com/brivanto.com.au.</li>
      <li>info@brivanto.com.au</li>
    </ul>
    <div class="contact-phone">0497 28 14 56</div>
  </article>
</section>

</body>
</html>
```